business card design for a plumbing contractor

i need a double business card for a plumbing business, our initial service is residential Sewer Drain Cleaning.

Target Market(s)

other plumbing Business

Industry/Entity Type

Plumbing

Contact Information for Business Card

www.PipeworksCrestline.example- 5817302946-

Font styles to use
Serif

Colors
ec1f27
0455a3

```html
<!DOCTYPE html>
<html lang="en">
<head>
<meta charset="utf-8">
<title>Pipeworks Crestline – Business Card</title>
<link rel="stylesheet" href="https://fonts.googleapis.com/css2?family=Roboto:wght@400;500;700&display=swap">
<style>
  :root {
    --backdrop: #2b2b2c;
    --card: #1c1c1d;
    --card-edge: #111112;
    --red: #e3262c;
    --white: #f2f2f2;
    --silver: #9c9ea1;
    --muted: #d8d8d8;
  }
  * { margin: 0; padding: 0; box-sizing: border-box; }
  html, body {
    width: 1200px; height: 900px; overflow: hidden;
    background: var(--backdrop);
    font-family: "Roboto", Arial, sans-serif;
  }
  .canvas { position: relative; width: 1200px; height: 900px; }
  .card {
    position: absolute; left: 250px; width: 700px; height: 400px;
    background: var(--card);
    border: 1px solid var(--card-edge);
  }
  .card--front { top: 40px; }
  .card--back { top: 470px; }

  .wordmark {
    display: flex; align-items: center; gap: 12px;
    font-weight: 700; line-height: 1.05;
  }
  .wordmark__square { width: 22px; height: 22px; flex: none; }
  .card--front .wordmark {
    position: absolute; left: 50%; top: 50%; transform: translate(-50%, -50%);
    color: var(--silver); font-size: 50px;
  }
  .card--front .wordmark__square { background: var(--silver); width: 30px; height: 30px; }

  .card--back .wordmark {
    position: absolute; left: 52px; top: 160px;
    color: var(--white); font-size: 34px;
  }
  .card--back .wordmark__square { background: var(--red); }

  .divider {
    position: absolute; left: 335px; top: 70px; width: 2px; height: 260px;
    background: var(--white);
  }
  .details { position: absolute; left: 362px; top: 82px; color: var(--white); }
  .person__name { color: var(--red); font-size: 30px; font-weight: 500; letter-spacing: 0.5px; }
  .person__role { font-size: 17px; color: var(--muted); margin-top: 2px; }
  .contact { list-style: none; margin-top: 16px; }
  .contact__item { display: flex; align-items: center; gap: 10px; font-size: 17px; line-height: 24px; }
  .contact__icon { width: 13px; height: 13px; flex: none; }
  .services { list-style: none; margin-top: 14px; }
  .services__item { display: flex; align-items: center; gap: 14px; font-size: 18px; line-height: 25px; }
  .services__item::before {
    content: ""; width: 8px; height: 8px; border-radius: 50%; background: var(--red); flex: none;
  }
</style>
</head>
<body>
<main class="canvas">
  <section class="card card--front" aria-label="Card front">
    <div class="wordmark">
      <span>Pipeworks<br>Crestline</span>
      <span class="wordmark__square" aria-hidden="true"></span>
    </div>
  </section>

  <section class="card card--back" aria-label="Card back">
    <div class="wordmark">
      <span>Pipeworks<br>Crestline</span>
      <span class="wordmark__square" aria-hidden="true"></span>
    </div>
    <div class="divider" aria-hidden="true"></div>
    <div class="details">
      <h1 class="person__name">DORIAN VALE</h1>
      <p class="person__role">Director</p>
      <ul class="contact">
        <li class="contact__item">
          <svg class="contact__icon" viewBox="0 0 24 24" aria-hidden="true"><path fill="#e3262c" d="M6.6 10.8a15.1 15.1 0 0 0 6.6 6.6l2.2-2.2a1 1 0 0 1 1-.25 11.4 11.4 0 0 0 3.6.57 1 1 0 0 1 1 1V20a1 1 0 0 1-1 1A17 17 0 0 1 3 4a1 1 0 0 1 1-1h3.5a1 1 0 0 1 1 1c0 1.25.2 2.45.57 3.57a1 1 0 0 1-.25 1z"/></svg>
          5817302946
        </li>
        <li class="contact__item">
          <svg class="contact__icon" viewBox="0 0 24 24" aria-hidden="true"><rect x="2" y="5" width="20" height="14" rx="1" fill="none" stroke="#e3262c" stroke-width="2"/><path d="M2 6l10 7 10-7" fill="none" stroke="#e3262c" stroke-width="2"/></svg>
          Dispatch@PipeworksCrestline.example
        </li>
        <li class="contact__item">
          <svg class="contact__icon" viewBox="0 0 24 24" aria-hidden="true"><g fill="none" stroke="#e3262c" stroke-width="2"><circle cx="12" cy="12" r="10"/><ellipse cx="12" cy="12" rx="4" ry="10"/><path d="M2 12h20"/></g></svg>
          www.PipeworksCrestline.example
        </li>
      </ul>
      <ul class="services">
        <li class="services__item">Sewer Drain Cleaning</li>
        <li class="services__item">Maintenance</li>
        <li class="services__item">Trenchless Pipe Installs.</li>
      </ul>
    </div>
  </section>
</main>
</body>
</html>
```